Flyer-Design für Fahrzeugpflege&Lackveredelung
Zielgruppe
Die Firma VK Glanzwerk - Fahrzeugpflege&Lackveredelung ist ein Kleinunternehmen im Car-Detailing Bereich. Hier steht höchste Qualität und maximale Kundenzufriedenheit auf höchster Stelle.
Zielgruppen sind Fahrzeugbesitzer von hochwertigen Wagen, die höchste Ansprüche auf die Fahrzeugaufbereitung legen.
Aber auch das Tagesgeschäft mit Innenraumaufbereitungen für den Normalverbraucher sind möglich.
Aufgabenstellung
Der Flyer soll modern und hochwertig aussehen.
Größe des Flyers: DIN lang (9,8x21)
2-seitig 4/4 farbig
Farben, Daten und Co bitte auf der Internetseite entnehmen
www.vkglanzwerk.de

```html
<!DOCTYPE html>
<html lang="de">
<head>
<meta charset="utf-8">
<title>VK Glanzwerk – Flyer</title>
<link rel="stylesheet" href="https://fonts.googleapis.com/css2?family=Raleway:wght@300;400;500;600;700;800&display=swap">
<style>
:root{
  --page:#f0f1f0;
  --paper:#ffffff;
  --ink:#4a4a4a;
  --blue:#2f6fc4;
  --blue-soft:#3b7bd0;
  --white:#ffffff;
}
*{margin:0;padding:0;box-sizing:border-box}
html,body{width:1200px;height:1200px;overflow:hidden;background:var(--page)}
body{font-family:"Raleway",sans-serif;font-variant-numeric:lining-nums;position:relative}
.flyer{position:absolute;left:357px;top:75px;width:487px;height:1042px;background:var(--paper);overflow:hidden}
.abs{position:absolute}
.headline{left:30px;top:34px;font-weight:800;font-size:24.5px;line-height:23.5px;color:var(--ink);letter-spacing:.2px}
.headline .accent{color:var(--blue)}
.brand{left:336px;top:42px;width:130px;display:flex;align-items:center;gap:6px}
.brand-dot{width:24px;height:24px;border:1.5px solid #222;flex:none}
.brand-text{color:#222;font-weight:400;font-size:12px;line-height:13px}
.brand-text small{display:block;font-size:6.5px;line-height:8px;letter-spacing:1px}
.tile{position:absolute;width:239px;height:159px;display:flex;align-items:center;justify-content:center}
.tile span{color:var(--white);font-weight:700;font-size:18.5px;text-shadow:0 1px 4px rgba(0,0,0,.45)}
.c1{left:0}.c2{left:248px}
.r1{top:101px}.r2{top:270px}.r3{top:439px}
.t-paint{background:linear-gradient(90deg,#6d6f78,#3a3a5c 45%,#8a8a90 55%,#2e2c4e)}
.t-coat{background:linear-gradient(135deg,#4a9bd8,#1f6bb0 55%,#0f3d6e)}
.t-interior{background:linear-gradient(160deg,#3b3b3b,#1e1e1e 50%,#5a3a28 65%,#2a2a2a)}
.t-upholstery{background:linear-gradient(90deg,#a8a6a2,#c9c7c3 50%,#d6d4d0)}
.t-leather{background:linear-gradient(135deg,#8a8a8a,#2e2e2e 40%,#3c3c3c)}
.t-repair{background:linear-gradient(135deg,#6a6a6a,#3a3a3a 50%,#b9a83c 85%,#4a4a4a)}
.bottom{position:absolute;left:0;top:646px;width:487px;height:396px}
.services{left:0;width:487px;top:618px;text-align:center}
.services .lead{font-size:14px;color:var(--ink);font-weight:400;margin-bottom:4px}
.services .list{font-size:12.5px;line-height:19.4px;font-weight:700;color:var(--blue)}
.offer{left:38px;color:var(--white)}
.offer-label{top:776px;font-weight:700;font-size:12.5px}
.price{top:788px;font-weight:600;font-size:68px;line-height:68px;letter-spacing:-1px}
.price .euro{font-size:30px;letter-spacing:0}
.price .star{position:absolute;left:117px;top:2px;font-size:16px}
.fine{top:858px;font-size:8.6px;line-height:10.5px;font-weight:400}
.owner{top:891px;font-weight:600;font-size:15px}
.address{top:918px;font-weight:400;font-size:15px;line-height:18px}
.contact{display:flex;align-items:center;gap:8px;color:var(--white);font-size:15px;font-weight:400}
.contact svg{width:14px;height:14px;flex:none}
.phone{left:37px;top:962px}
.mail{left:37px;top:989px}
.social{left:220px;top:961px;font-weight:500}
.social .ring{width:14px;height:14px;border:1.8px solid var(--white);border-radius:50%;flex:none}
.web{left:221px;top:988px;font-weight:600;font-size:14.5px;color:var(--white)}
</style>
</head>
<body>
<main class="flyer">
  <h1 class="abs headline">WAS KANN ICH FÜR<br><span class="accent">DEIN FAHRZEUG</span> TUN?</h1>
  <div class="abs brand">
    <span class="brand-dot"></span>
    <div class="brand-text">VK Glanzwerk<small>Fahrzeugpflege</small><small>Lackveredelung</small></div>
  </div>

  <div class="tile c1 r1 t-paint" role="img" aria-label="Foto: Vorher-Nachher einer Lackkorrektur an dunklem Lack"><span>Lackkorrektur</span></div>
  <div class="tile c2 r1 t-coat" role="img" aria-label="Foto: Front eines blauen Sportwagens mit glänzendem Lack"><span>Lackveredelung</span></div>
  <div class="tile c1 r2 t-interior" role="img" aria-label="Foto: Vorher-Nachher einer Mittelkonsole"><span>Innenraumreinigung</span></div>
  <div class="tile c2 r2 t-upholstery" role="img" aria-label="Foto: Vorher-Nachher eines Stoffsitzes"><span>Polsterreinigung</span></div>
  <div class="tile c1 r3 t-leather" role="img" aria-label="Foto: gereinigter schwarzer Ledersitz"><span>Lederreinigung</span></div>
  <div class="tile c2 r3 t-repair" role="img" aria-label="Foto: abgeklebter Ledersitz bei der Reparatur"><span>Lederreparatur</span></div>

  <svg class="bottom" viewBox="0 0 487 396" aria-hidden="true">
    <defs>
      <linearGradient id="blueFade" x1="0" y1="0" x2="0" y2="1">
        <stop offset="0" stop-color="#3576c9"/>
        <stop offset="1" stop-color="#3a7ccf"/>
      </linearGradient>
      <linearGradient id="studio" x1="0" y1="0" x2="1" y2="1">
        <stop offset="0" stop-color="#8a7a68"/>
        <stop offset=".5" stop-color="#c9c4bd"/>
        <stop offset="1" stop-color="#9ea6ad"/>
      </linearGradient>
    </defs>
    <rect width="487" height="396" fill="url(#blueFade)"/>
    <polygon points="0,0 487,0 245,123" fill="#ffffff"/>
    <polygon points="245,123 487,0 487,249" fill="url(#studio)" role="img" aria-label="Foto: Werkstatthalle mit Lichtdecke und Fahrzeugen"/>
  </svg>

  <div class="abs services">
    <p class="lead">Weitere Leistungen:</p>
    <p class="list">Scheibenversiegelung | Leasingrückläufer<br>Geruchsbeseitigung | Cabriodachimprägnierung<br>Scheinwerferaufbereitung<br>uvm.</p>
  </div>

  <p class="abs offer offer-label">AUSSENAUFBEREITUNG AB</p>
  <p class="abs offer price">299<span class="euro">€</span><span class="star">*</span></p>
  <p class="abs offer fine">*Alle Preise orientieren sich an einem<br>gepflegten Fahrzeug im Neuwagenzustand.</p>
  <p class="abs offer owner">Inh. Kai Vollmer</p>
  <p class="abs offer address">Am Werkhof 4<br>34590 Wabern</p>

  <div class="abs contact phone">
    <svg viewBox="0 0 24 24"><path fill="#fff" d="M6.6 10.8a15.2 15.2 0 0 0 6.6 6.6l2.2-2.2a1 1 0 0 1 1-.25 11.4 11.4 0 0 0 3.6.57 1 1 0 0 1 1 1V20a1 1 0 0 1-1 1A17 17 0 0 1 3 4a1 1 0 0 1 1-1h3.5a1 1 0 0 1 1 1c0 1.25.2 2.45.57 3.57a1 1 0 0 1-.25 1z"/></svg>
    <span>+49 170 000 1234</span>
  </div>
  <div class="abs contact mail">
    <svg viewBox="0 0 24 24"><path fill="#fff" d="M2 5h20v14H2z"/><path fill="none" stroke="#3a7ccf" stroke-width="2" d="M2.5 5.5 12 13l9.5-7.5"/></svg>
    <span>info@vkglanzwerk.de</span>
  </div>
  <div class="abs contact social"><span class="ring"></span><span>vk.glanzwerk</span></div>
  <p class="abs web">www.vkglanzwerk.de</p>
</main>
</body>
</html>
```